Launch Website

A very simple, but attractive website (template preferred) is required in a common format - HTML5 or Wordpress etc.
It should be easily user updateable for updates.
Pages it needs:
-Home Page with menu bar, company logo and 1 large graphic/picture and two smaller graphics/logos.
- What we do
- How we do it
- About Us
- Guarantees
- Results
- Contact Page with Enquiry Form
- Provision for a blog to be added later

Most pages will be approx 150 words text with some small/medium images.
We have our own domain & hosting.

A "less is more" design approach would be encouraged.

Target Market(s)

Vehicle Fleet Managers

Industry/Entity Type

It Company

Font styles to use
Sans Serif

Colors
9bcb3c

Requirements
Must have
• Corporate Style. No Fluff.
Nice to have
• Images of LIght Commerical vehicles and trucks

Am ok with white background throughout site.
Colours should match/complement company logo.
Should not have
• Should not be too "busy"

```html
<!DOCTYPE html>
<html lang="en">
<head>
<meta charset="utf-8">
<title>Harborline Transit – Steady Mileage</title>
<link rel="stylesheet" href="https://fonts.googleapis.com/css2?family=Roboto:wght@400;500&family=PT+Sans+Narrow:wght@400;700&family=Arimo:wght@400;700&display=swap">
<style>
  :root{
    --green:#0a9a48;
    --green-dark:#079441;
    --blue:#1f7fd2;
    --blue-band:#2a86d6;
    --ink:#4a4a4a;
    --muted:#808080;
    --white:#ffffff;
    --badge:#cfd3d6;
  }
  *{margin:0;padding:0;box-sizing:border-box}
  html,body{width:891px;height:1200px;overflow:hidden;background:var(--white)}
  body{position:relative;font-family:"Roboto",Arial,sans-serif}
  .abs{position:absolute}

  .brand{left:22px;top:14px;display:inline-block;text-align:right}
  .brand-name{font-family:"Roboto",sans-serif;font-weight:400;font-size:40px;letter-spacing:1px;color:var(--green);line-height:1;white-space:nowrap}
  .brand-tagline{font-size:14.5px;letter-spacing:.5px;color:#333;white-space:nowrap;margin-top:6px}
  .partner-shape{left:620px;top:47px;width:132px;height:29px;border-radius:7px;background:var(--badge)}
  .partner-badge{left:773px;top:28px;width:92px;height:44px;border-radius:4px;background:var(--badge)}

  .side-band{left:0;top:88px;width:891px;height:286px;background:var(--blue)}
  .nav{left:0;top:88px;width:891px;height:39px;list-style:none}
  .nav li{color:var(--white);font-size:14px;line-height:39px;position:absolute;top:0;white-space:nowrap}
  .nav .active{background:var(--green);left:18px;width:92px;text-align:center}
  .hero-frame{left:16px;top:127px;width:857px;height:356px;background:var(--white)}
  .hero{left:24px;top:134px;width:841px;height:340px;background:linear-gradient(100deg,#c7b64a 0%,#e7d66a 22%,#9aa05a 40%,#d8d8df 55%,#b8bcc8 75%,#5e6d3a 100%)}

  .feature{width:400px;height:80px}
  .feature svg{position:absolute;left:0;top:0}
  .feature h3{position:absolute;left:75px;top:0;font-family:"PT Sans Narrow",sans-serif;font-weight:700;font-size:16.5px;color:var(--ink);white-space:nowrap}
  .feature p{position:absolute;left:75px;top:21px;width:300px;font-family:"PT Sans Narrow",sans-serif;font-size:12px;line-height:15.5px;color:var(--muted)}

  .testimonials{left:0;top:715px;width:891px;height:283px;background:radial-gradient(ellipse at 30% 70%,#3a8fd6 0%,var(--blue-band) 45%,#2681d2 100%)}
  .testimonials-title{left:0;top:745px;width:891px;text-align:center;font-family:"PT Sans Narrow",sans-serif;font-weight:700;font-size:34px;color:var(--white)}
  .avatar{width:43px;height:43px;background:linear-gradient(#c9d4de,#8a9aac);border:2px solid #e8eef4}
  .quote{width:322px;height:91px;background:var(--white);font-family:"Arimo",sans-serif;font-size:11.3px;line-height:13.3px;color:#111;padding:13px 15px}
  .quote::before{content:"";position:absolute;left:-18px;top:16px;border-right:18px solid var(--white);border-bottom:14px solid transparent}
  .person{font-family:"Arimo",sans-serif;color:var(--white)}
  .person b{display:block;font-size:12.7px}
  .person span{font-size:11px;color:#cfe2f4}

  .footer{left:0;top:997px;width:891px;height:203px;background:var(--green-dark)}
  .social{left:0;top:1046px;width:891px;display:flex;justify-content:center;gap:12px;padding-left:6px}
  .social span{width:40px;height:40px;border-radius:50%;background:var(--white)}
  .footer-links{left:0;top:1128px;width:891px;text-align:center;font-family:"Arimo",sans-serif;font-size:11.5px;color:var(--white)}
  .copyright{left:0;top:1146px;width:891px;text-align:center;font-family:"Arimo",sans-serif;font-size:10px;color:var(--white)}
</style>
</head>
<body>
  <header>
    <div class="abs brand">
      <div class="brand-name">HARBORLINE TRANSIT</div>
      <div class="brand-tagline">STEADY MILEAGE</div>
    </div>
    <div class="abs partner-shape" role="img" aria-label="Partner badge"></div>
    <div class="abs partner-badge" role="img" aria-label="Association membership badge"></div>
  </header>

  <div class="abs side-band"></div>
  <ul class="abs nav">
    <li class="active">HOME</li>
    <li style="left:133px">WHAT WE DO</li>
    <li style="left:267px">HOW WE DO IT</li>
    <li style="left:410px">ABOUT US</li>
    <li style="left:526px">GUARANTEES</li>
    <li style="left:661px">RESULTS</li>
    <li style="left:767px">CONTACT US</li>
  </ul>
  <div class="abs hero-frame"></div>
  <div class="abs hero" role="img" aria-label="Truck driving along a sunlit country road"></div>

  <section>
    <div class="abs feature" style="left:49px;top:511px">
      <svg width="60" height="54" viewBox="0 0 60 54"><rect x="0" y="12" width="15" height="31" fill="var(--green)"/><rect x="22" y="26" width="15" height="17" fill="var(--green)"/><rect x="44" y="0" width="15" height="43" fill="var(--green)"/><rect x="0" y="48" width="59" height="4" fill="var(--green)"/></svg>
      <h3>Progress to Trial</h3>
      <p>Lorem ipsum dolor sit amet, consectetuer adipiscing elit, sed diam nonummy nibh euismod tincidunt ut laoreet dolore magna aliquam erat volutpat. Ut wisi enim ad minim veniam, quis nostrud.</p>
    </div>
    <div class="abs feature" style="left:490px;top:511px">
      <svg width="60" height="56" viewBox="0 0 60 56"><path d="M38 4H8a5 5 0 0 0-5 5v38a5 5 0 0 0 5 5h40a5 5 0 0 0 5-5V22" fill="none" stroke="var(--green)" stroke-width="5"/><path d="M50 0l8 8-26 26-11 3 3-11z" fill="var(--green)"/></svg>
      <h3>Assess Trial Results</h3>
      <p>Adipiscing elit, sed diam nonummy nibh euismod tincidunt ut laoreet dolore magna aliquam erat volutpat. Ut wisi enim ad minim veniam, quis nostrud exerci tation ullamcorper.</p>
    </div>
    <div class="abs feature" style="left:49px;top:612px">
      <svg width="60" height="44" viewBox="0 0 60 44"><rect x="0" y="2" width="36" height="30" rx="2" fill="var(--green)"/><path d="M38 10h12l9 11v11H38z" fill="var(--green)"/><circle cx="11" cy="36" r="6" fill="var(--green)" stroke="#fff" stroke-width="3"/><circle cx="48" cy="36" r="6" fill="var(--green)" stroke="#fff" stroke-width="3"/></svg>
      <h3>Rollout to balance of Fleet</h3>
      <p>Diam nonummy nibh euismod tincidunt ut laoreet dolore magna aliquam erat volutpat. Ut wisi enim ad minim veniam, quis nostrud exerci tation ullamcorper suscipit lobortis nisl ut aliquip ex.</p>
    </div>
    <div class="abs feature" style="left:490px;top:612px">
      <svg width="57" height="57" viewBox="0 0 57 57"><rect x="2" y="2" width="53" height="53" fill="none" stroke="var(--green)" stroke-width="4"/><rect x="2" y="2" width="53" height="12" fill="var(--green)"/><rect x="7" y="6" width="3" height="3" fill="#fff"/><rect x="13" y="6" width="3" height="3" fill="#fff"/><rect x="19" y="6" width="3" height="3" fill="#fff"/><path d="M10 40l8-10 8 10 8-12 6 8 6-5" fill="none" stroke="var(--green)" stroke-width="4"/></svg>
      <h3>Monitor ongoing cost savings</h3>
      <p>Lorem ipsum dolor sit amet, consectetuer adipiscing elit, sed diam nonummy nibh euismod tincidunt ut laoreet dolore magna aliquam erat volutpat. Ut wisi enim ad minim veniam.</p>
    </div>
  </section>

  <section>
    <div class="abs testimonials" role="img" aria-label="Soft blue background photo of smiling customers"></div>
    <h2 class="abs testimonials-title">Our Testimonials</h2>

    <div class="abs avatar" style="left:32px;top:833px" role="img" aria-label="Portrait of Dan Mercer"></div>
    <div class="abs quote" style="left:101px;top:816px">"Lorem ipsum dolor sit amet, consectetuer adipiscing elit, sed diam nonummy nibh euismod tincidunt ut laoreet dolore magna aliquam erat volutpat. Ut wisi enim ad minim veniam, quis nostrud exerci tation ullamcorper suscipit lobortis nisl ut aliquip ex ea commodo consequat."</div>
    <div class="abs person" style="left:102px;top:917px"><b>Dan Mercer</b><span>Founder, Mercer Studio</span></div>

    <div class="abs avatar" style="left:459px;top:833px" role="img" aria-label="Portrait of L. Hartley"></div>
    <div class="abs quote" style="left:527px;top:816px">"Lorem ipsum dolor sit amet, consectetuer adipiscing elit, sed diam nonummy nibh euismod tincidunt ut laoreet dolore magna aliquam erat volutpat. Ut wisi enim ad minim veniam, quis nostrud exerci tation ullamcorper suscipit lobortis nisl ut aliquip ex ea commodo consequat."</div>
    <div class="abs person" style="left:528px;top:917px"><b>L. Hartley</b><span>Marketer of Senior Products</span></div>
  </section>

  <footer>
    <div class="abs footer"></div>
    <div class="abs social"><span></span><span></span><span></span><span></span><span></span></div>
    <div class="abs footer-links">Home · About Us · Products · Features · Options · Replacement Parts · FAQ's · Library · Videos · Contact Us</div>
    <div class="abs copyright">© Copyright 2002 - 2013 Company Name. All Rights Reserved</div>
  </footer>
</body>
</html>
```